Orbel Appraisals website redesign

I would like to refresh my existing website of www.orbelappraisals-demo.com with new graphics, look and feel, as well as updated structure and wording. Content and layout changes have been uploaded to this project Brief.

My existing website has a dark feel. I am now looking for a light and energetic feel. Financial Services is my industry, so the website should be reflect that. I would also like to reflect the concepts of Trust, Service and Expertise.

The website must be serious and upmarket.

Target Market(s)

Corporate board members, CFO's, treasurers and controllers
Auditors, tax advisors, private equity and venture capital asset managers, investors, tax authorities

Industry/Entity Type

Financial Service

Coding

Coded - Design and coding required

Number of Pages Required

5+ page

Font styles to use
Sans Serif
Other font styles liked:
• Designer can choose another modern font

Colors
0355a3
3277b5
85acd3
eaf1f7
f37122
f68d4d
9bcb3c
acd037
cadf82

Requirements
Must have
• Good hi resolution pictures that convey "Finance", "Trust", "Service" or "Expertise".
• An anti-bot (such as Captcha) mechanism in the contact form.
Should not have
• Must not have all content on one rolling screen.

```html
<!DOCTYPE html>
<html lang="en">
<head>
<meta charset="utf-8">
<title>Orbel Appraisals – Business &amp; Intellectual Property Valuations</title>
<link rel="stylesheet" href="https://fonts.googleapis.com/css2?family=Montserrat:wght@300;400;600;700&family=Work+Sans:wght@400;500;600&display=swap">
<style>
:root{
  --blue:#0355a3;
  --blue-mid:#3277b5;
  --blue-soft:#85acd3;
  --blue-pale:#eaf1f7;
  --orange:#f37122;
  --orange-soft:#f68d4d;
  --green:#9bcb3c;
  --ink:#2b2f36;
  --dark:#161d2a;
  --white:#fff;
}
*{box-sizing:border-box;margin:0;padding:0}
html,body{width:1200px;height:3843px;overflow:hidden}
body{position:relative;font-family:"Work Sans",Arial,sans-serif;color:var(--ink);background:var(--white)}
.abs{position:absolute}
.heading-font{font-family:"Montserrat",Arial,sans-serif}

/* header */
.site-header{top:0;left:0;width:1200px;height:78px;background:var(--white)}
.brand{left:124px;top:22px;font-family:"Montserrat",Arial,sans-serif;font-weight:600;font-size:20px;color:var(--ink);display:flex;align-items:center;gap:10px}
.brand-dot{width:14px;height:14px;background:var(--orange)}
.main-nav{top:30px;left:454px;display:flex;gap:0;font-size:15px}
.main-nav a{color:var(--ink);text-decoration:none;position:absolute;white-space:nowrap}
.main-nav .active{color:var(--orange)}
.btn{display:inline-flex;align-items:center;justify-content:center;background:var(--orange);color:var(--white);font-family:"Montserrat",Arial,sans-serif;font-weight:600;font-size:14px;text-decoration:none}
.nav-cta{left:947px;top:18px;width:129px;height:42px;font-size:15px;font-weight:400;font-family:"Work Sans",Arial,sans-serif}

/* hero */
.hero{top:78px;left:0;width:1200px;height:600px;background:linear-gradient(90deg,#6b6660 0%,#5c5550 40%,#3f3c3c 70%,#50565e 100%)}
.hero-shade{inset:0;background:rgba(20,20,25,.35)}
.hero-title{top:188px;left:0;width:1200px;text-align:center;color:var(--white);font-family:"Montserrat",Arial,sans-serif;line-height:62px}
.hero-title .light{display:block;font-weight:300;font-size:60px}
.hero-title .bold{display:block;font-weight:700;font-size:60px}
.hero-text{top:344px;left:0;width:1200px;text-align:center;color:var(--white);font-size:15px;line-height:26px}
.hero-cta{top:429px;left:536px;width:128px;height:42px}

/* section titles */
.section-title{left:0;width:1200px;text-align:center;font-family:"Montserrat",Arial,sans-serif;font-size:24px;font-weight:400;letter-spacing:.5px}
.section-title b{font-weight:700}
.section-mark{width:14px;height:14px;background:var(--blue-soft)}
.title-rule{height:2px;width:57px}

/* services */
.services{top:678px;left:0;width:1200px;height:587px;background:var(--blue);color:var(--white)}
.service-card{top:202px;width:299px;height:299px;text-align:center}
.service-card.featured{border:2px solid var(--orange)}
.service-icon{width:52px;height:52px;border-radius:50%;background:var(--orange);margin:32px auto 0;display:flex;align-items:center;justify-content:center}
.service-card h3{font-family:"Montserrat",Arial,sans-serif;font-weight:600;font-size:25px;line-height:31px;margin-top:18px;padding:0 40px}
.service-card p{font-size:12.5px;line-height:26px;margin-top:12px;padding:0 24px;color:#dce7f3}
.slider-arrow{width:14px;height:14px}

/* about */
.about{top:1265px;left:0;width:1200px;height:650px;background:linear-gradient(90deg,#f7f7f7,#fbfbfb 60%,#f3f4f6)}
.about-photo{left:694px;top:-25px;width:382px;height:590px;background:linear-gradient(160deg,#9a8f84,#5e5a57 55%,#b9b2a7);border-top:8px solid var(--orange);border-bottom:8px solid var(--orange)}
.about-heading{left:124px;top:112px;font-family:"Montserrat",Arial,sans-serif;font-size:23px;color:var(--orange);letter-spacing:.5px}
.about-heading b{font-weight:700}
.about-body{left:124px;top:180px;width:470px;font-size:14.5px;line-height:31px}
.about-body p+p{margin-top:10px}
.about-body .small{line-height:26px}
.about-body .lead{font-weight:500;font-size:16px;line-height:31px}
.about-cta{left:124px;top:523px;width:129px;height:41px;font-size:13px}

/* expertise */
.expertise-photo{top:1915px;left:2px;width:529px;height:397px;background:linear-gradient(135deg,#d8dde2,#9ba7b3 55%,#e5e7ea)}
.expertise{top:1915px;left:531px;width:669px;height:397px;background:var(--blue);color:var(--white)}
.expertise h2{position:absolute;left:80px;top:83px;font-family:"Montserrat",Arial,sans-serif;font-weight:600;font-size:24px}
.expertise .lead{position:absolute;left:80px;top:133px;width:480px;font-size:15px;line-height:26px}
.expertise ul{position:absolute;left:80px;top:202px;list-style:none;font-size:12.5px}
.expertise li{height:31px;padding-left:30px;position:relative}
.expertise li::before{content:"";position:absolute;left:0;top:5px;border-left:5px solid var(--white);border-top:4px solid transparent;border-bottom:4px solid transparent}

/* news */
.news-card{top:2520px;width:300px}
.news-image{height:145px}
.news-date{margin-top:32px;font-size:11px;color:var(--green);letter-spacing:1px;text-transform:uppercase}
.news-text{margin-top:18px;font-size:15px;line-height:22px;letter-spacing:.3px}
.news-text.link{color:var(--orange);text-decoration:underline}

/* contact form */
.help{top:2876px;left:124px;width:952px;height:496px;background:var(--blue);color:var(--white)}
.field{background:#eeeeee;color:#9a9a9a;font-size:12px;padding:0 16px;display:flex;align-items:center;letter-spacing:.5px}
.field.area{align-items:flex-start;padding-top:14px}
.send{width:44px;height:44px;border-radius:50%;background:var(--orange);display:flex;align-items:center;justify-content:center}

/* footer */
.site-footer{top:3372px;left:0;width:1200px;height:405px;background:var(--dark);color:#c5cad3}
.site-footer h4{position:absolute;top:62px;font-family:"Montserrat",Arial,sans-serif;font-weight:600;font-size:19px;color:var(--white)}
.contact-list{position:absolute;left:124px;top:110px;font-size:12.5px;line-height:20px}
.contact-list dt{color:var(--white);font-weight:500;display:flex;align-items:center;gap:5px}
.contact-list dd{margin-bottom:22px}
.quick-links{position:absolute;left:450px;top:110px;list-style:none;font-size:12.5px;line-height:26px}
.quick-links .active{color:var(--orange)}
.footer-map{position:absolute;left:776px;top:112px;width:300px;height:222px;background:linear-gradient(135deg,#e7ecf1,#d9e3ec 50%,#eef2f5)}
.bottom-bar{top:3777px;left:0;width:1200px;height:66px;background:var(--blue);color:var(--white);font-size:12px}
.social{width:33px;height:33px;border-radius:50%}
</style>
</head>
<body>

<header class="site-header abs">
  <div class="brand abs"><span class="brand-dot"></span>Orbel Appraisals</div>
  <nav class="main-nav abs">
    <a class="active" style="left:0">Home</a>
    <a style="left:96px">About us</a>
    <a style="left:218px">Services</a>
    <a style="left:333px">News &amp; Views</a>
  </nav>
  <a class="btn nav-cta abs">Contact us</a>
</header>

<section class="hero abs" role="img" aria-label="Photo of advisers meeting a client across a desk with a laptop">
  <div class="hero-shade abs"></div>
  <h1 class="hero-title abs"><span class="light">Business &amp; Intellectual</span><span class="bold">Property Valuations</span></h1>
  <p class="hero-text abs">Trust is paramount. Clients rely on Orbel Appraisal Services<br>for confidentiality, transparency and independence.</p>
  <a class="btn hero-cta abs">Contact us</a>
</section>

<section class="services abs">
  <div class="section-mark abs" style="left:593px;top:86px"></div>
  <h2 class="section-title abs" style="top:112px">OUR <b>SERVICES</b></h2>
  <div class="title-rule abs" style="left:572px;top:160px;background:var(--blue-soft)"></div>

  <svg class="slider-arrow abs" style="left:40px;top:345px" viewBox="0 0 14 14"><path d="M9 2 4 7l5 5" fill="none" stroke="#fff" stroke-width="2"/></svg>
  <svg class="slider-arrow abs" style="left:1137px;top:345px" viewBox="0 0 14 14"><path d="M5 2l5 5-5 5" fill="none" stroke="#fff" stroke-width="2"/></svg>

  <article class="service-card abs" style="left:122px">
    <div class="service-icon"><svg width="22" height="22" viewBox="0 0 22 22"><path d="M4 18V11M9 18V6M14 18V9M19 18V4M2 19h18" stroke="#fff" stroke-width="2" fill="none"/></svg></div>
    <h3>Business Valuation</h3>
    <p>Company stakeholders trust Orbel Appraisals to provide business valuations for transaction, accounting,</p>
  </article>
  <article class="service-card featured abs" style="left:450px">
    <div class="service-icon"><svg width="22" height="22" viewBox="0 0 22 22"><rect x="5" y="3" width="12" height="16" rx="1" stroke="#fff" stroke-width="2" fill="none"/><path d="M8 8h6M8 12h6M8 16h4" stroke="#fff" stroke-width="1.6"/></svg></div>
    <h3>Business Plan Coaching</h3>
    <p>Young companies and entrepreneurs frequently ask for our advice on their business plans and strategies.</p>
  </article>
  <article class="service-card abs" style="left:776px">
    <div class="service-icon"><svg width="22" height="22" viewBox="0 0 22 22"><path d="M3 17l5-5 4 3 7-8" stroke="#fff" stroke-width="2" fill="none"/><path d="M14 7h5v5" stroke="#fff" stroke-width="2" fill="none"/></svg></div>
    <h3>M&amp;A Advisory</h3>
    <p>Business valuations to support Dutch participation exemption, capital gains and significant interest tests</p>
  </article>
</section>

<section class="about abs">
  <div class="about-photo abs" role="img" aria-label="Photo of two colleagues smiling at a laptop in an office"></div>
  <div class="section-mark abs" style="left:220px;top:86px;background:var(--orange-soft)"></div>
  <h2 class="about-heading abs">ABOUT <b>COMPANY</b></h2>
  <div class="about-body abs">
    <p>Service is front and center in Orbel Appraisal Services’ product offerings. Orbel Appraisal Services considers the needs of all stakeholders and the personal needs of the client team involved.</p>
    <p class="small">Orbel Appraisal Services offers more than a decade of valuation experience and maintains its commitment to continual professional development.</p>
    <p class="lead">Trust is paramount. Clients rely on Orbel Appraisal Services for confidentiality, transparency and independence.</p>
  </div>
  <a class="btn about-cta abs">Read More</a>
</section>

<div class="expertise-photo abs" role="img" aria-label="Photo of two businessmen shaking hands over a desk"></div>
<section class="expertise abs">
  <h2>We are an expert in this field</h2>
  <p class="lead">Lorem ipsum dolor sit amet, consectetur adipiscing elit, sed do eiusmod tempor incididunt.</p>
  <ul>
    <li>Duis aute irure dolor in reprehenderit</li>
    <li>Duis aute irure dolor in reprehenderit</li>
    <li>Excepteur sint occaecat cupidatat</li>
    <li>Sed ut perspiciatis unde omnis iste natus error.</li>
  </ul>
</section>

<div class="section-mark abs" style="left:593px;top:2402px;background:var(--orange-soft)"></div>
<h2 class="section-title abs" style="top:2428px;color:var(--orange)">OUR <b>NEWS</b></h2>
<div class="title-rule abs" style="left:572px;top:2475px;background:var(--orange)"></div>
<svg class="slider-arrow abs" style="left:40px;top:2585px" viewBox="0 0 14 14"><path d="M9 2 4 7l5 5" fill="none" stroke="#222" stroke-width="2"/></svg>
<svg class="slider-arrow abs" style="left:1137px;top:2585px" viewBox="0 0 14 14"><path d="M5 2l5 5-5 5" fill="none" stroke="#222" stroke-width="2"/></svg>

<article class="news-card abs" style="left:124px">
  <div class="news-image" role="img" aria-label="Photo of a tablet showing financial charts beside a coffee cup" style="background:linear-gradient(135deg,#f2f2f2,#cfd6dc)"></div>
  <p class="news-date">March 9, 2016</p>
  <p class="news-text">A number of Dutch GAAP accounting changes took effect on January 1, 2016 more then part.</p>
</article>
<article class="news-card abs" style="left:450px">
  <div class="news-image" role="img" aria-label="Photo of stacked shipping containers against the sky" style="background:linear-gradient(135deg,#5a6d80,#b5583c 60%,#c96a4a)"></div>
  <p class="news-date">February 4, 2016</p>
  <p class="news-text link">At $265 billion, the Netherlands is the 3rd largest foreign investor in the United States.</p>
</article>
<article class="news-card abs" style="left:776px">
  <div class="news-image" role="img" aria-label="Photo of a street sign on a financial district corner" style="background:linear-gradient(135deg,#d9d9d9,#7c7c7c 55%,#c2c2c2)"></div>
  <p class="news-date">February 4, 2016</p>
  <p class="news-text">Leiden, 2 februari 2016 – Martin Hale, managing director van Orbel Appraisals, presenteert.</p>
</article>

<section class="help abs">
  <div class="section-mark abs" style="left:469px;top:86px"></div>
  <h2 class="section-title abs" style="top:112px;left:0;width:952px">HOW CAN <b>WE HELP?</b></h2>
  <div class="title-rule abs" style="left:448px;top:160px;background:var(--blue-soft)"></div>
  <div class="field abs" style="left:64px;top:200px;width:273px;height:34px">Name</div>
  <div class="field abs" style="left:357px;top:200px;width:274px;height:34px">Email</div>
  <div class="field abs" style="left:648px;top:200px;width:206px;height:34px">Phone</div>
  <div class="field area abs" style="left:66px;top:251px;width:788px;height:128px">How can we help? ...</div>
  <div class="send abs" style="left:764px;top:367px"><svg width="18" height="18" viewBox="0 0 18 18"><path d="M2 9 16 2 12 16 9 10z" fill="#fff"/></svg></div>
</section>

<footer class="site-footer abs">
  <h4 style="left:124px">Contact Us</h4>
  <h4 style="left:450px">Quick Links</h4>
  <h4 style="left:776px">Get The Direction</h4>
  <dl class="contact-list">
    <dt><svg width="9" height="12" viewBox="0 0 9 12"><path d="M4.5 0A4.5 4.5 0 0 0 0 4.5C0 8 4.5 12 4.5 12S9 8 9 4.5A4.5 4.5 0 0 0 4.5 0zm0 6.5a2 2 0 1 1 0-4 2 2 0 0 1 0 4z" fill="#fff"/></svg>Address:</dt>
    <dd>Keizerslaan 24, 2311<br>BK Leiden, The Netherlands</dd>
    <dt><svg width="11" height="11" viewBox="0 0 11 11"><path d="M2 0l2 3-1 1.5a7 7 0 0 0 3.5 3.5L8 7l3 2-1 2C5 11 0 6 0 1z" fill="#fff"/></svg>Phone:</dt>
    <dd>+31 70 555 0142</dd>
    <dt><svg width="11" height="9" viewBox="0 0 11 9"><rect width="11" height="9" fill="#fff"/><path d="M0 0l5.5 5L11 0" stroke="#161d2a" fill="none"/></svg>Email:</dt>
    <dd>info@orbelappraisals-demo.com</dd>
  </dl>
  <ul class="quick-links">
    <li>Home</li>
    <li class="active">About us</li>
    <li>Services</li>
    <li>News &amp; Views</li>
    <li>Contact us</li>
  </ul>
  <div class="footer-map" role="img" aria-label="Street map showing the office location in Leiden"></div>
</footer>

<div class="bottom-bar abs">
  <p class="abs" style="left:124px;top:26px">©2019 Orbel Appraisals, Website by Nordlane Web Studio.</p>
  <p class="abs" style="left:776px;top:26px;font-weight:500">Stay Connected With Us:</p>
  <span class="social abs" style="left:956px;top:16px;background:var(--blue-mid)" role="img" aria-label="Social profile"></span>
  <span class="social abs" style="left:999px;top:16px;background:var(--blue-soft)" role="img" aria-label="Social profile"></span>
  <span class="social abs" style="left:1043px;top:16px;background:var(--orange)" role="img" aria-label="Social profile"></span>
</div>

</body>
</html>
```